Clear Summit Vitality Label Designs

I am looking for a label design for my supplements called "Clear Summit Vitality." I am looking for a label that is contemporary, and gender-neutral and that fits well with my product logo. I have 50 products so it would have to be versatile enough to change out the product names.
Choose the labels that fit best. NHB, GMP, third party tested, USA the most important.
Colors chosen are points of reference, be creative, have fun.

Target Market(s)

health minded consumers. Both men and women, so gender neutral.

Colors
9bcb3c
3176b5

Requirements
Must have
• Coloring that is in line with my logo. Contempory. Stamdard supplent panel for ingrsupplement facts, suggested use, general safety, disclaimers, logo, small decals for NHB, GMP, etc, I can provide them if necessary, lot # expiration date, lot number,

```html
<!DOCTYPE html>
<html lang="en">
<head>
<meta charset="utf-8">
<title>Clear Summit Vitality – Glucosamine Chondroitin MSM</title>
<link href="https://fonts.googleapis.com/css2?family=Exo+2:wght@400;600;700&display=swap" rel="stylesheet">
<style>
  :root {
    --label-blue: #1f80c6;
    --label-blue-light: #3a90cf;
    --brand-blue: #2a73b8;
    --ink: #1b1b1b;
    --white: #ffffff;
  }
  html, body {
    margin: 0;
    padding: 0;
    overflow: hidden;
    background: var(--white);
  }
  .label {
    position: relative;
    width: 1200px;
    height: 2400px;
    overflow: hidden;
    font-family: "Exo 2", sans-serif;
    text-align: center;
  }
  .backdrop {
    position: absolute;
    inset: 0;
    background: radial-gradient(ellipse at 50% 55%, var(--label-blue-light) 0%, var(--label-blue) 70%);
  }
  .front-panel {
    position: absolute;
    left: 180px;
    top: 0;
    width: 840px;
    height: 1310px;
    background: var(--white);
  }
  .brand {
    position: absolute;
    left: 0;
    right: 0;
    top: 170px;
  }
  .brand-name {
    margin: 0;
    font-size: 88px;
    font-weight: 600;
    line-height: 1.0;
    color: var(--brand-blue);
  }
  .brand-tagline {
    margin: 14px 0 0;
    font-size: 31px;
    font-weight: 600;
    font-style: italic;
    color: var(--brand-blue);
  }
  .product-name {
    position: absolute;
    left: 0;
    right: 0;
    top: 838px;
    margin: 0;
    font-size: 116px;
    font-weight: 700;
    line-height: 144px;
    color: var(--ink);
  }
  .category {
    position: absolute;
    left: 0;
    right: 0;
    top: 1345px;
    margin: 0;
    font-size: 90px;
    font-weight: 400;
    color: var(--white);
  }
  .benefits {
    position: absolute;
    left: 0;
    right: 0;
    top: 1532px;
    margin: 0;
    padding: 0;
    list-style: none;
    font-size: 65px;
    line-height: 78px;
    color: var(--ink);
  }
  .benefits li { margin-bottom: 40px; }
  .assurances {
    position: absolute;
    left: 0;
    right: 0;
    top: 2055px;
    margin: 0;
    font-size: 49px;
    line-height: 76px;
    color: var(--white);
    text-transform: uppercase;
  }
  .count-band {
    position: absolute;
    left: 0;
    right: 0;
    bottom: 0;
    height: 173px;
    background: var(--white);
    display: flex;
    align-items: center;
    justify-content: center;
  }
  .count {
    margin: 0;
    font-size: 80px;
    font-weight: 400;
    color: var(--brand-blue);
    letter-spacing: 1px;
  }
</style>
</head>
<body>
<main class="label">
  <div class="backdrop" role="img" aria-label="Soft blue swirl pattern background"></div>

  <section class="front-panel">
    <div class="brand">
      <p class="brand-name">Clear Summit<br>Vitality</p>
      <p class="brand-tagline">Renewing the world one body at a time</p>
    </div>
    <h1 class="product-name">Glucosamine<br>Chondroitin<br>MSM</h1>
  </section>

  <p class="category">mobility</p>

  <ul class="benefits">
    <li>strengthens joint tissues</li>
    <li>improves flexibility</li>
    <li>supports production of<br>healthy joint structures</li>
  </ul>

  <p class="assurances">Made in a NHB-registered facility<br>Premium quality&nbsp; / &nbsp;Third party tested</p>

  <footer class="count-band">
    <p class="count">120 CAPSULES</p>
  </footer>
</main>
</body>
</html>
```